Small Business Consulting Firm Needs Business Card Design

Need a sleek modern business card with 2 sides matching the colors of our logo. We will be placing these with a mailer we are sending out. These business cards will only ever be given to business owners. We operate helping businesses who are struggling with cash flow or finances. If the green and blue design needs to be moved to the right of "Harborline Crest Consulting" for aesthetic purposes that is ok. We will need an editable file if possible. We would like to include the reps name, email, website, and phone number. For now just use Peter Vance, pvance@harborlinecrest.com, www.harborlinecrest.com, and 833-555-0172.

```html
<!DOCTYPE html>
<html lang="en">
<head>
<meta charset="utf-8">
<title>Harborline Crest Consulting – Business Card</title>
<link href="https://fonts.googleapis.com/css2?family=Open+Sans:wght@400;600&family=Arimo:wght@400;700&display=swap" rel="stylesheet">
<style>
  :root {
    --bg: #e9e9eb;
    --card: #ffffff;
    --ink: #454545;
    --ink-soft: #333333;
    --blue: #1a7cc5;
    --navy: #135f96;
    --green: #5f9e35;
  }
  * { margin: 0; padding: 0; box-sizing: border-box; }
  html, body { width: 1200px; height: 900px; overflow: hidden; background: var(--bg); }
  .canvas { position: relative; width: 1200px; height: 900px; }
  .card {
    position: absolute; left: 250px; width: 700px; height: 400px;
    background: var(--card); overflow: hidden;
    box-shadow: 0 6px 18px rgba(0,0,0,.12);
  }
  .card--front { top: 40px; }
  .card--back { top: 470px; }

  .brand { display: flex; align-items: center; gap: 22px; font-family: "Open Sans", sans-serif; font-weight: 400; color: var(--ink); }
  .brand__mark { background: var(--green); flex: none; }
  .brand__name { line-height: 1.05; text-transform: uppercase; white-space: nowrap; }
  .brand__line2 { display: block; letter-spacing: .42em; }

  .card--front .brand { position: absolute; left: 50%; top: 50%; transform: translate(-50%,-50%); }
  .card--front .brand__mark { width: 70px; height: 70px; }
  .card--front .brand__name { font-size: 44px; }
  .card--front .brand__line2 { font-size: 22px; margin-top: 10px; }

  .band { position: absolute; inset: 0; }
  .card--back .brand { position: absolute; right: 130px; top: 46px; gap: 12px; }
  .card--back .brand__mark { width: 30px; height: 30px; }
  .card--back .brand__name { font-size: 20px; }
  .card--back .brand__line2 { font-size: 10px; margin-top: 4px; }

  .rep { position: absolute; left: 80px; top: 150px; font-family: "Arimo", sans-serif; }
  .rep__name { font-size: 40px; font-weight: 700; letter-spacing: -.5px; }
  .rep__first { color: var(--blue); }
  .rep__last { color: var(--green); }
  .rep__title { font-size: 19px; color: var(--ink-soft); margin-top: 2px; margin-left: 18px; }
  .accent-bar { position: absolute; left: 0; top: 242px; width: 36px; height: 36px; background: var(--blue); }

  .contact { position: absolute; left: 90px; top: 272px; font-family: "Arimo", sans-serif; font-size: 18px; color: var(--ink-soft); list-style: none; }
  .contact::before { content: ""; display: block; width: 26px; height: 3px; background: var(--green); margin-bottom: 10px; }
  .contact__item { display: flex; align-items: center; gap: 12px; height: 27px; white-space: nowrap; }
  .contact__icon { width: 18px; height: 18px; fill: var(--blue); flex: none; }
</style>
</head>
<body>
<main class="canvas">
  <section class="card card--front" aria-label="Card front">
    <div class="brand">
      <span class="brand__mark"></span>
      <p class="brand__name">Harborline Crest<span class="brand__line2">Consulting</span></p>
    </div>
  </section>

  <section class="card card--back" aria-label="Card back">
    <svg class="band" width="700" height="400" viewBox="0 0 700 400">
      <path d="M700 30 C650 230 560 340 380 400 L700 400 Z" fill="var(--navy)"/>
      <path d="M700 30 C650 230 560 340 380 400" fill="none" stroke="var(--green)" stroke-width="7"/>
    </svg>
    <div class="brand">
      <span class="brand__mark"></span>
      <p class="brand__name">Harborline Crest<span class="brand__line2">Consulting</span></p>
    </div>
    <span class="accent-bar"></span>
    <div class="rep">
      <p class="rep__name"><span class="rep__first">Peter</span> <span class="rep__last">Vance</span></p>
      <p class="rep__title">owners</p>
    </div>
    <ul class="contact">
      <li class="contact__item">
        <svg class="contact__icon" viewBox="0 0 24 24"><path d="M6.6 10.8a15.1 15.1 0 0 0 6.6 6.6l2.2-2.2a1 1 0 0 1 1-.25 11.4 11.4 0 0 0 3.6.57 1 1 0 0 1 1 1V20a1 1 0 0 1-1 1A17 17 0 0 1 3 4a1 1 0 0 1 1-1h3.5a1 1 0 0 1 1 1c0 1.25.2 2.450.57 3.57a1 1 0 0 1-.25 1z"/></svg>
        <span>833-555-0172</span>
      </li>
      <li class="contact__item">
        <svg class="contact__icon" viewBox="0 0 24 24"><path d="M2 5h20v14H2z M3 6l9 7 9-7" stroke="#fff" stroke-width="1.4"/></svg>
        <span>pvance@harborlinecrest.com</span>
      </li>
      <li class="contact__item">
        <svg class="contact__icon" viewBox="0 0 24 24"><circle cx="12" cy="12" r="10"/><path d="M2 12h20M12 2c3 3 3 17 0 20M12 2c-3 3-3 17 0 20" stroke="#fff" stroke-width="1.4" fill="none"/></svg>
        <span>www.harborlinecrest.com</span>
      </li>
    </ul>
  </section>
</main>
</body>
</html>
```